Nonprofit Postcard Design

We need a postcard designed to raise awareness and donations for a Nonprofit called "RWL Memorial". We are a new nonprofit that gives out scholarships to high school seniors. In 2005 my brother, Marcus Dale Hollins, was taken from my family in a violent act of crime. My family has formed a scholarship foundation, RWL Memorial Scholarship, in memory of my brother. This scholarship fund will help seniors who want to go to college by giving them money that can aide in the cost of books, tuition, or housing. We would like to give two scholarships per year, and we need your help to make that possible. Marcus was a loving and very kind person who would help anyone who needed it. He was a member of the Pine Ridge High School Band and a very academically involved student who planned to go to college. We are remembering him through this scholarship. We are a non-profit organization, so all donations are tax deductible. Each year, students will receive a scholarship, along with a certificate which will list all company logos that have donated to make this scholarship one that can last for many years to come. www.rwlmemorial-example.org

Industry/Entity Type

High School

```html
<!DOCTYPE html>
<html lang="en">
<head>
<meta charset="utf-8">
<title>RWL Memorial Nonprofit Postcard</title>
<link rel="stylesheet" href="https://fonts.googleapis.com/css2?family=PT+Sans:ital,wght@0,400;0,700;1,400;1,700&family=Roboto+Condensed:ital,wght@1,300&family=Tinos&display=swap">
<style>
  :root {
    --navy: #1b3550;
    --navy-bar: #1f3f5b;
    --slate: #5d6a75;
    --yellow: #f6ec34;
    --blue: #1f6fb7;
    --blue-light: #5aa6e8;
    --page: #e9ecef;
    --card: #ffffff;
    --sky: #dcebf8;
  }
  * { box-sizing: border-box; margin: 0; padding: 0; }
  html, body { width: 1200px; height: 1074px; overflow: hidden; }
  body { background: var(--page); position: relative; font-family: "PT Sans", sans-serif; color: var(--navy); }

  .card { position: absolute; width: 680px; height: 528px; background: var(--card); overflow: hidden; }
  .card--back { left: 40px; top: 6px;
    background: radial-gradient(ellipse 520px 300px at 560px 60px, var(--sky), transparent 70%),
                radial-gradient(ellipse 420px 220px at 120px 500px, #eef5fc, transparent 70%), var(--card); }
  .card--front { left: 480px; top: 540px; }

  .wordmark { position: absolute; display: flex; align-items: center; gap: 10px;
    font-family: "PT Sans", sans-serif; font-weight: 700; color: var(--navy); line-height: 1.1; }
  .wordmark__dot { flex: none; border-radius: 50%; background: var(--navy); }

  .back__logo { left: 24px; top: 62px; width: 160px; font-size: 18px; }
  .back__logo .wordmark__dot { width: 14px; height: 14px; }
  .back__title { position: absolute; left: 192px; top: 30px; font-family: "Tinos", serif; font-weight: 400; font-size: 27px; line-height: 32px; color: var(--navy); white-space: nowrap; }
  .back__tagline { position: absolute; left: 194px; top: 68px; width: 310px; font-family: "Roboto Condensed", sans-serif; font-style: italic; font-weight: 300; font-size: 16.5px; color: var(--slate); white-space: nowrap; }
  .back__intro { position: absolute; left: 194px; top: 98px; width: 300px; font-size: 14.5px; line-height: 18.5px; }
  .stamp-box { position: absolute; left: 518px; top: 27px; width: 142px; height: 136px; border: 1px solid #c9d6e2; background: rgba(255,255,255,.45); }
  .portrait { position: absolute; left: 25px; top: 172px; width: 60px; height: 82px; background: linear-gradient(160deg, #2c3f8f, #111826 70%); }
  .story { position: absolute; font-size: 12.5px; line-height: 16.5px; }
  .story--lead { left: 100px; top: 168px; width: 220px; }
  .story--more { left: 25px; top: 266px; width: 300px; }

  .donate { position: absolute; border-radius: 50%; display: flex; align-items: center; justify-content: center; text-align: center;
    color: #fff; line-height: 1; background: radial-gradient(circle at 50% 30%, var(--blue-light), var(--blue) 60%, #154f87);
    border: 4px solid #fff; box-shadow: 0 0 0 2px #c4d3e0; }
  .back__donate { left: 24px; top: 354px; width: 74px; height: 74px; font-size: 14.5px; }
  .back__contact { position: absolute; left: 114px; top: 364px; }
  .back__contact h2 { font-size: 19px; font-style: italic; font-weight: 700; margin-bottom: 4px; }
  .back__contact p { font-size: 14.5px; line-height: 19px; }

  .front__photo { position: absolute; left: 300px; top: 0; width: 380px; height: 452px;
    background: linear-gradient(100deg, #ffffff 0%, #e8e3dc 18%, #c99a7d 45%, #9bb7d2 62%, #e7c98d 78%, #7fbf6a 100%); }
  .front__logo { left: 46px; top: 92px; width: 240px; font-size: 24px; }
  .front__logo .wordmark__dot { width: 20px; height: 20px; }
  .front__copy { position: absolute; left: 46px; top: 228px; width: 248px; font-size: 18px; line-height: 23px; }
  .front__heading { display: flex; align-items: center; gap: 8px; }
  .readers-icon { width: 70px; height: 28px; background: var(--navy-bar); border-radius: 14px 14px 4px 4px; }
  .front__copy strong { display: block; font-style: italic; font-weight: 700; font-size: 21px; line-height: 26px; white-space: nowrap; }
  .front__copy p + p { margin-top: 23px; }
  .front__band { position: absolute; left: 0; top: 452px; width: 680px; height: 36px; background: var(--yellow);
    padding-left: 46px; font-size: 19px; font-style: italic; font-weight: 700; line-height: 36px; }
  .front__bar { position: absolute; left: 0; top: 488px; width: 680px; height: 40px; background: var(--navy-bar);
    color: #fff; font-size: 13px; line-height: 40px; text-align: center; white-space: nowrap; }
  .front__bar span { margin: 0 7px; }
  .front__donate { left: 568px; top: 392px; width: 86px; height: 86px; font-size: 17px; }
  .front__arrow { position: absolute; left: 560px; top: 452px; }
</style>
</head>
<body>

<section class="card card--back" aria-label="Postcard back">
  <div class="wordmark back__logo"><span class="wordmark__dot"></span>RWL Memorial Scholarship</div>
  <h1 class="back__title">RWL Memorial Nonprofit</h1>
  <p class="back__tagline">Scholarships for East Texas High school Seniors</p>
  <p class="back__intro">We are a local Nonprofit that is dedicated to give back to the local community, In Loving memory of Marcus Hollins.</p>
  <div class="stamp-box" aria-label="Stamp area"></div>
  <div class="portrait" role="img" aria-label="Portrait photo of Marcus Dale Hollins"></div>
  <p class="story story--lead">In 2005 my brother, Marcus Dale Hollins, was taken from my family in a violent act of crime. My family has formed a scholarship foundation, RWL Memorial Scholarship, in memory of my brother.</p>
  <p class="story story--more">This scholarship fund will help seniors who want to go to college by giving them money that can aide in the cost of books, tuition, or housing. We would like to give two scholarships per year, and we need your help to make that possible.</p>
  <div class="donate back__donate">Donate<br>Now</div>
  <div class="back__contact">
    <h2>Contact us today!</h2>
    <p>DanielHollins@rwlmemorial-example.org</p>
    <p>www.rwlmemorial-example.org</p>
  </div>
</section>

<section class="card card--front" aria-label="Postcard front">
  <div class="front__photo" role="img" aria-label="Photo of smiling graduating students holding a diploma"></div>
  <div class="wordmark front__logo"><span class="wordmark__dot"></span>RWL Memorial Scholarship</div>
  <div class="front__copy">
    <p><span class="front__heading">RWL Memorial <span class="readers-icon" role="img" aria-label="Illustration of two students reading"></span></span>
      <strong>Nonprofit Corporation's</strong>
      purpose is to provide scholarships to East Texas High School Seniors.</p>
    <p>Aiding local high school Seniors that have a will power to continue their education.</p>
  </div>
  <div class="front__band">To learn more, contact us today!</div>
  <div class="front__bar">PO Box 4410 Cedar Falls, TX 75999<span>|</span>DanielHollins@rwlmemorial-example.org<span>|</span>www.rwlmemorial-example.org</div>
  <svg class="front__arrow" width="22" height="32" viewBox="0 0 22 32" aria-hidden="true">
    <path d="M16 2 C8 8 8 18 10 28 M4 22 L10 29 L15 21" fill="none" stroke="#1b3550" stroke-width="2" stroke-linecap="round"/>
  </svg>
  <div class="donate front__donate">Donate<br>Now</div>
</section>

</body>
</html>
```